Design Business Cards for my forest, wood company

Hi ,
I need that you create Business Card and for my forest, wood company
display on it Name Surname , job position(Director) , the type of work we do (logging ,woodworking) ,
telephone number , email ,
and our adress with bank account which is written togehter in 4 rows
example for adress and bank account it has to be together ,
Reg.Nr. 718290537
Pilvena Mustod Ka
Toliksa Brevins LE-8715
KVP LE71MOTR0004817566

Suggested colors are Green , yellow , black , brown

also you need to add,create nice looking and simple logo with my bussines name which has some kind of icon or symbol, picture . I add logo example what I want in it , three icons in one there is trees , in other there is wood planks and in third ear field .
My company name "ĶIRBĒLU DOMASTES"

I add my bussines name in picture format , because it includes signs which are not in english.
I add Business card example which I like , it has everything I mentioned .

If any question please ask , if I will see business card which I like will award it immediately .

```html
<!DOCTYPE html>
<html lang="en">
<head>
<meta charset="utf-8">
<title>Ķirbēlu Domastes – Business Card</title>
<link rel="stylesheet" href="https://fonts.googleapis.com/css2?family=Fira+Sans:wght@400;600;700&family=Fira+Sans+Condensed:wght@600;700&display=swap">
<style>
  :root {
    --page: #ffffff;
    --card: #f4b878;
    --band: #9a6a55;
    --band-text: #f6c68c;
    --tagline: #f7dab0;
    --mark: #7fae3a;
    --ink: #1c140f;
    --name: #f7c890;
    --name-shade: #8a5a3c;
    --wood-dark: #8c4b2c;
    --wood-mid: #b56a43;
    --wood-light: #c98559;
    --shadow: rgba(0,0,0,0.35);
  }
  html, body {
    margin: 0;
    padding: 0;
    width: 1200px;
    height: 373px;
    overflow: hidden;
    background: var(--page);
  }
  .canvas {
    position: relative;
    width: 1200px;
    height: 373px;
    font-family: "Fira Sans", Arial, sans-serif;
  }
  .card {
    position: absolute;
    top: 53px;
    width: 500px;
    height: 280px;
    background: var(--card);
    box-shadow: 4px 5px 4px var(--shadow);
    overflow: hidden;
  }
  .card--front { left: 36px; }
  .card--back { left: 607px; }

  .brand-mark {
    position: absolute;
    left: 40px;
    top: 110px;
    width: 80px;
    height: 86px;
    box-sizing: border-box;
    border: 2px solid var(--mark);
  }
  .brand-band {
    position: absolute;
    left: 131px;
    top: 110px;
    width: 369px;
    height: 86px;
    background: var(--band);
  }
  .brand-name {
    position: absolute;
    left: 16px;
    top: 12px;
    margin: 0;
    font-family: "Fira Sans", Arial, sans-serif;
    font-weight: 400;
    font-size: 27px;
    letter-spacing: 1.5px;
    color: var(--band-text);
    white-space: nowrap;
  }
  .brand-services {
    position: absolute;
    left: 93px;
    top: 48px;
    margin: 0;
    font-size: 20px;
    font-weight: 400;
    letter-spacing: 0.5px;
    color: var(--tagline);
    white-space: nowrap;
  }

  .wood-panel {
    position: absolute;
    left: 0;
    top: 0;
    width: 500px;
    height: 138px;
    background: linear-gradient(100deg, var(--wood-dark) 0%, var(--wood-mid) 35%, var(--wood-light) 60%, var(--wood-mid) 80%, var(--wood-dark) 100%);
  }
  .person-name {
    position: absolute;
    right: 6px;
    top: 100px;
    margin: 0;
    font-family: "Fira Sans Condensed", Arial, sans-serif;
    font-weight: 600;
    font-size: 40px;
    letter-spacing: 1px;
    color: var(--name);
    text-shadow: 1px 1px 0 var(--name-shade), 2px 2px 2px rgba(0,0,0,0.3);
    white-space: nowrap;
  }
  .person-role {
    position: absolute;
    right: 6px;
    top: 144px;
    margin: 0;
    font-family: "Fira Sans Condensed", Arial, sans-serif;
    font-weight: 700;
    font-size: 17px;
    color: var(--ink);
  }
  .company-details {
    position: absolute;
    left: 8px;
    top: 206px;
    margin: 0;
    font-size: 11.5px;
    font-weight: 600;
    line-height: 17.5px;
    color: var(--ink);
    text-transform: uppercase;
  }
  .contact-list {
    position: absolute;
    left: 297px;
    top: 209px;
    margin: 0;
    padding: 0;
    list-style: none;
    font-size: 11.5px;
    font-weight: 600;
    color: var(--ink);
  }
  .contact-list li {
    display: flex;
    align-items: center;
    height: 21px;
  }
  .contact-list svg {
    width: 13px;
    height: 13px;
    margin-right: 6px;
    flex: none;
  }
</style>
</head>
<body>
<div class="canvas">

  <section class="card card--front">
    <div class="brand-mark"></div>
    <div class="brand-band">
      <h1 class="brand-name">ĶIRBĒLU DOMASTES</h1>
      <p class="brand-services">logging ,woodworking</p>
    </div>
  </section>

  <section class="card card--back">
    <div class="wood-panel" role="img" aria-label="Wood grain texture in warm brown tones"></div>
    <h2 class="person-name">MAREK OSVIN</h2>
    <p class="person-role">DIRECTOR</p>

    <p class="company-details">
      Reg.Nr. 718290537<br>
      Pilvena Mustod Ka<br>
      Toliksa Brevins LE-8715<br>
      KVP LE71MOTR0004817566
    </p>

    <ul class="contact-list">
      <li>
        <svg viewBox="0 0 16 16" aria-hidden="true">
          <circle cx="8" cy="8" r="7" fill="none" stroke="#1c140f" stroke-width="1.4"/>
          <path d="M5.2 4.2 L6.6 4 L7.2 6 L6.3 6.8 Q7 8.6 9 9.6 L9.9 8.8 L11.8 9.4 L11.6 10.8 Q9.5 12.2 6.8 9.6 Q4.3 7 5.2 4.2 Z" fill="#1c140f"/>
        </svg>
        02417586390 , 0241758639
      </li>
      <li>
        <svg viewBox="0 0 16 16" aria-hidden="true">
          <circle cx="8" cy="8" r="7" fill="none" stroke="#1c140f" stroke-width="1.4"/>
          <rect x="4" y="5.3" width="8" height="5.6" fill="none" stroke="#1c140f" stroke-width="1.2"/>
          <path d="M4 5.5 L8 8.6 L12 5.5" fill="none" stroke="#1c140f" stroke-width="1.2"/>
        </svg>
        INFO@KIRBELUDOMASTES.COM
      </li>
      <li>
        <svg viewBox="0 0 16 16" aria-hidden="true">
          <circle cx="8" cy="8" r="7" fill="none" stroke="#1c140f" stroke-width="1.4"/>
          <ellipse cx="8" cy="8" rx="3" ry="7" fill="none" stroke="#1c140f" stroke-width="1.1"/>
          <path d="M1.2 8 H14.8 M2.5 4.5 H13.5 M2.5 11.5 H13.5" stroke="#1c140f" stroke-width="1.1"/>
        </svg>
        WWW.KIRBELUDOMASTES.COM
      </li>
    </ul>
  </section>

</div>
</body>
</html>
```